Web Design Project

Please take a look at my current aged website www.tarlowpeopleadvisory.com and my newly designed logo and business cards. I would like a new fresh updated look to my website and my new designs incorporated.
Updates

  Good Morning Everyone

Due to an Austrralian licencing issue I have had to have my logo slightly redesigned.

Would you please be able to look at the newly uploaded files and revise your designs.

Thanks so much.  I am very happy with the calibre and quality of the designs so far.

kind Regards

Marnie

Industry/Entity Type

Business

Requirements
Must have
• the exisiting pages and fresh new graphics and a real commitment to my palette of lime green, turqouise and black.

```html
<!DOCTYPE html>
<html lang="en">
<head>
<meta charset="utf-8">
<title>Tarlow People Advisory – Our Fees</title>
<link rel="stylesheet" href="https://fonts.googleapis.com/css2?family=Arimo:wght@400&family=Roboto+Condensed:wght@400&family=Source+Sans+3:wght@400;500&display=swap">
<style>
  :root {
    --backdrop: #9a9a9a;
    --sheet: #ffffff;
    --lime: #6db83b;
    --lime-pale: #d7e0d2;
    --turquoise: #38a9cf;
    --ink: #111111;
    --ink-soft: #555555;
    --grey-soft: #8c8c8c;
    --dial-rim: #cfcfcf;
    --dial-face: #e4e4e4;
  }
  * { margin: 0; padding: 0; box-sizing: border-box; }
  html, body { width: 1082px; height: 1200px; overflow: hidden; background: var(--backdrop); }
  .stage { position: relative; width: 1012px; height: 1122px; transform: scale(1.0692, 1.0695); transform-origin: 0 0; }
  .sheet {
    position: absolute; left: 175px; top: 10px; width: 661px; height: 1066px;
    background: var(--sheet); box-shadow: 0 2px 9px 3px rgba(0,0,0,.55); overflow: hidden;
  }
  .sheet-strip {
    position: absolute; left: 0; top: 0; width: 22px; height: 100%;
    background: linear-gradient(to bottom, #e3e8e0 0%, #cfdcc6 35%, #9ccb7a 70%, var(--lime) 100%);
  }
  .masthead { position: absolute; left: 22px; top: 0; width: 639px; height: 220px; }
  .brand-mark { position: absolute; left: 45px; top: 35px; width: 94px; height: 94px; border: 5px solid var(--turquoise); border-radius: 50%; }
  .brand-name { position: absolute; left: 145px; top: 18px; font: 400 33px/1 "Arimo", sans-serif; color: var(--ink); letter-spacing: -0.3px; }
  .brand-tagline { position: absolute; left: 202px; top: 57px; font: 400 13px/1 "Arimo", sans-serif; color: var(--grey-soft); }
  .main-nav a {
    position: absolute; font: 400 17.5px/1 "Roboto Condensed", sans-serif; color: var(--ink-soft);
    text-decoration: none; white-space: nowrap;
  }
  .main-nav .is-active { color: var(--ink); }
  .fees-pill {
    position: absolute; left: 641px; top: 256px; width: 100px; height: 28px;
    background: linear-gradient(to right, #c9d8c0, #dfe7db); border-radius: 6px 0 0 6px;
  }
  .section-band {
    position: absolute; left: 22px; top: 264px; width: 460px; height: 30px;
    background: linear-gradient(to right, var(--lime-pale) 0%, var(--lime-pale) 70%, rgba(255,255,255,0) 100%);
  }
  .section-title { position: absolute; left: 83px; top: 268px; font: 400 20px/1 "Roboto Condensed", sans-serif; color: var(--ink); }
  .team-photo {
    position: absolute; left: 81px; top: 315px; width: 222px; height: 148px;
    background: linear-gradient(135deg, #2b3444 0%, #6b7486 40%, #dfe3ea 65%, #28303d 100%);
  }
  .copy { position: absolute; left: 80px; top: 477px; width: 500px; font: 400 15.5px/20px "Source Sans 3", sans-serif; color: var(--ink); }
  .copy p + p { margin-top: 40px; }
  .footer-band {
    position: absolute; left: 22px; top: 1009px; width: 639px; height: 57px;
    background: linear-gradient(to right, var(--lime-pale) 0%, var(--lime-pale) 50%, #ffffff 100%);
  }
  .dial { position: absolute; left: 710px; top: 140px; width: 190px; height: 190px; }
  .foot-nav { position: absolute; left: 199px; top: 1087px; display: flex; font: 400 15.5px/1 "Source Sans 3", sans-serif; }
  .foot-nav a { color: #fff; text-decoration: none; padding: 5px 9px; border-left: 1px solid #fff; }
  .foot-nav a:first-child { border-left: none; }
  .copyright { position: absolute; left: 703px; top: 1092px; font: 400 15px/1 "Source Sans 3", sans-serif; color: #fff; text-shadow: 1px 1px 1px #333; }
</style>
</head>
<body>
<div class="stage">
  <div class="sheet">
    <div class="sheet-strip"></div>
    <svg class="masthead" viewBox="0 0 639 220" aria-hidden="true">
      <defs>
        <linearGradient id="mastheadFill" x1="0" y1="0" x2="0.3" y2="1">
          <stop offset="0" stop-color="#f2f2f2"/>
          <stop offset="1" stop-color="#cfcfcf"/>
        </linearGradient>
      </defs>
      <path d="M0 0 H639 V88 C450 110 220 150 0 210 Z" fill="url(#mastheadFill)"/>
      <path d="M0 210 C220 150 450 110 639 88" fill="none" stroke="#bdbdbd" stroke-width="2"/>
    </svg>
    <div class="brand-mark"></div>
    <div class="brand-name">Tarlow People Advisory</div>
    <div class="brand-tagline">Outsourced Human Resources Solutions and Stragedies</div>
    <div class="section-band"></div>
    <h1 class="section-title">Our Consultants</h1>
    <div class="team-photo" role="img" aria-label="Photo of business people shaking hands in an office"></div>
    <div class="copy">
      <p>Our highly competitive fees will be tailored to suit your organisation’s individual needs.&nbsp; Generally the Consultant’s time will be charged at an hourly rate however some projects will require the Consultant to work on a retainer or an agreed fixed fee for a specific project and these rates may be negotiated.</p>
      <p>Fees, Terms and Conditions and a Service Level Agreement will be discussed and negotiated at your initial no-obligation<br>on-site consultation.</p>
    </div>
    <div class="footer-band"></div>
  </div>

  <div class="fees-pill"></div>
  <svg class="dial" viewBox="0 0 190 190" aria-hidden="true">
    <circle cx="91" cy="91" r="83" fill="var(--dial-rim)" stroke="#a9a9a9" stroke-width="2"/>
    <circle cx="91" cy="91" r="66" fill="#f4f4f4"/>
    <circle cx="91" cy="91" r="60" fill="var(--dial-face)"/>
    <circle cx="91" cy="91" r="74" fill="none" stroke="var(--turquoise)" stroke-width="14"
            stroke-dasharray="14 4 14 4 14 4 14 4 0 465" transform="rotate(-130 91 91)" opacity=".9"/>
    <circle cx="91" cy="91" r="74" fill="none" stroke="#e8e8e8" stroke-width="9"
            stroke-dasharray="13 5 13 5 13 5 13 5 0 465" transform="rotate(-129 91 91)"/>
    <circle cx="91" cy="91" r="74" fill="none" stroke="var(--lime)" stroke-width="12"
            stroke-dasharray="18 447" transform="rotate(152 91 91)"/>
    <path d="M48 143 A74 74 0 0 0 134 143" fill="none" stroke="var(--turquoise)" stroke-width="3"/>
    <circle cx="91" cy="91" r="26" fill="none" stroke="#fff" stroke-width="3"/>
  </svg>

  <nav class="main-nav">
    <a href="#" style="left:700px;top:153px">Home</a>
    <a href="#" style="left:632px;top:185px">Our Services</a>
    <a href="#" class="is-active" style="left:601px;top:222px">Our Consultants</a>
    <a href="#" style="left:656px;top:260px">Our Fees</a>
    <a href="#" style="left:751px;top:317px">Contact Us</a>
  </nav>

  <nav class="foot-nav">
    <a href="#">Home</a>
    <a href="#">Our Services</a>
    <a href="#">Our Consultants</a>
    <a href="#">Our Fees</a>
    <a href="#">Contact Us</a>
  </nav>
  <div class="copyright">Copyright 2012 ©</div>
</div>
</body>
</html>
```